FotoVELTA buisnesscard

Hey :) I need a modern buisnesscard for my company FotoVELTA
It most have:
Dagligleder og Fotograf: Henrik Torvald Bjelland

Mob: +4791642058
Epost: post@fotovelta.no
Adresse: Bakkestien22, 5412 Solvik

Facbook and instagram logo with text FotoVELTA

FotoVELTA logo

It Company

```html
<!DOCTYPE html>
<html lang="no">
<head>
<meta charset="utf-8">
<title>FotoVELTA – visittkort</title>
<link href="https://fonts.googleapis.com/css2?family=Raleway:wght@300;400;600;700&display=swap" rel="stylesheet">
<style>
  :root{
    --page:#d9d9d9;
    --front-bg:#0b0b0b;
    --front-pattern-a:#1c1c1c;
    --front-pattern-b:#0b0b0b;
    --brand-light:#bdbdbd;
    --back-bg:#e6e6e6;
    --back-pattern:#ececec;
    --ink:#3a3a3a;
    --ink-soft:#9a9a9a;
    --icon-bg:#8a8a8a;
    --rule:#a8a8a8;
    --band:#c9c9c9;
    --chip:#4a4a4a;
    --faint:#cfcfcf;
  }
  *{box-sizing:border-box;margin:0;padding:0}
  html,body{width:1200px;height:900px;overflow:hidden}
  body{
    background:var(--page);
    font-family:"Raleway",sans-serif;
    position:relative;
  }
  .card{
    position:absolute;left:285px;width:630px;height:360px;
    overflow:hidden;box-shadow:0 4px 18px rgba(0,0,0,.18);
  }
  .card--front{top:60px;background:var(--front-bg)}
  .card--back{top:480px;background:var(--back-bg)}

  .front-pattern{
    position:absolute;inset:0;
    background:radial-gradient(ellipse at 50% 50%,var(--front-pattern-a),var(--front-pattern-b) 70%);
  }
  .front-brand{
    position:absolute;left:0;right:0;top:50%;transform:translateY(-50%);
    text-align:center;color:var(--brand-light);
    font-weight:700;font-size:58px;letter-spacing:1px;
  }

  .back-pattern{
    position:absolute;inset:0;
    background:radial-gradient(ellipse at 55% 40%,var(--back-pattern),var(--back-bg) 70%);
  }
  .guide-line{
    position:absolute;left:56px;top:0;width:2px;height:100%;background:var(--rule);
  }
  .guide-line--contacts{left:207px;top:120px;height:240px;width:1px}
  .back-watermark{
    position:absolute;left:68px;bottom:48px;
    color:var(--faint);font-weight:700;font-size:24px;
  }
  .role{
    position:absolute;right:40px;top:34px;
    color:var(--ink-soft);font-weight:400;font-size:19px;
  }
  .person{
    position:absolute;right:40px;top:58px;
    color:var(--ink);font-weight:400;font-size:25px;
  }
  .contacts{position:absolute;left:190px;top:112px;list-style:none}
  .contact{display:flex;align-items:center;gap:16px;height:48px}
  .contact-icon{
    width:34px;height:34px;border-radius:5px;background:var(--icon-bg);
    display:flex;align-items:center;justify-content:center;
  }
  .contact-text{color:var(--ink);font-size:20px;letter-spacing:.5px}
  .social-band{
    position:absolute;right:0;top:258px;width:300px;height:32px;background:var(--band);
  }
  .social{
    position:absolute;display:flex;align-items:center;gap:6px;
    height:32px;padding:0 12px;border-radius:8px;
    font-weight:700;font-size:17px;
  }
  .social--one{right:172px;top:292px;background:var(--chip);color:#eee}
  .social--two{right:14px;top:258px;color:var(--chip)}
  .social-dot{width:14px;height:14px;border-radius:3px;background:currentColor;opacity:.8}
</style>
</head>
<body>
  <section class="card card--front">
    <div class="front-pattern" role="img" aria-label="Overlappende mørke diagonale bånd i bakgrunnen"></div>
    <div class="front-brand">FotoVELTA</div>
  </section>

  <section class="card card--back">
    <div class="back-pattern" role="img" aria-label="Svake lyse diagonale bånd i bakgrunnen"></div>
    <div class="guide-line"></div>
    <div class="guide-line guide-line--contacts"></div>
    <div class="back-watermark">FotoVELTA</div>

    <p class="role">Dagligleder og Fotograf:</p>
    <h1 class="person">Henrik Torvald Bjelland</h1>

    <ul class="contacts">
      <li class="contact">
        <span class="contact-icon">
          <svg width="14" height="22" viewBox="0 0 14 22"><rect x="1" y="1" width="12" height="20" rx="2" fill="none" stroke="#333" stroke-width="1.6"/><line x1="5" y1="18" x2="9" y2="18" stroke="#333" stroke-width="1.6"/></svg>
        </span>
        <span class="contact-text">+4791642058</span>
      </li>
      <li class="contact">
        <span class="contact-icon">
          <svg width="22" height="16" viewBox="0 0 22 16"><rect x="1" y="1" width="20" height="14" fill="#333"/><polyline points="1,1 11,9 21,1" fill="none" stroke="#8a8a8a" stroke-width="1.6"/></svg>
        </span>
        <span class="contact-text">post@fotovelta.no</span>
      </li>
      <li class="contact">
        <span class="contact-icon">
          <svg width="16" height="22" viewBox="0 0 16 22"><path d="M8 21 C3 14 1 11 1 8 A7 7 0 0 1 15 8 C15 11 13 14 8 21Z" fill="#333"/><circle cx="8" cy="8" r="2.6" fill="#8a8a8a"/></svg>
        </span>
        <span class="contact-text">Bakkestien22, 5412 Solvik</span>
      </li>
    </ul>

    <div class="social-band"></div>
    <div class="social social--one"><span class="social-dot"></span>FotoVELTA</div>
    <div class="social social--two"><span class="social-dot"></span>FotoVELTA</div>
  </section>
</body>
</html>
```